Innovation Company Business Card Design

I need to have my business card updated. The current card was designed when the company started 2.5 years ago and was a quick and dirty job.

I need a new card design that is more professional and has my updated company tag line.

I will include the old card's Corel Draw file, and EPS versions as examples of the current design. I will also include the company logo eps and corel version files.

The company pantone colour is pantone 1805 c (a dark red)

I want the design to convey the nature of our business as a strategic technology innovation company, but yet still be professional. We are funky vibey and work from an industrial style office in a vibey designer dominat part of town. Though are clients include large banks and corporate clients too.

The information that needs to be on the card is in attached word document (but doesn't have to be in this order or format)

Final version needs to be supplied in PNG preview, as well as PSD file format (or other editable file version) so that personal information on card can be easily edited and reprinted.

Target Market(s)

CEO's of small to medium size companies
Marketing Managers of large coporates
Account managers of Digital Agencies

Industry/Entity Type

Business

Requirements
Must have
• 86x54mm will be cut in rounded corner credit card size format (Except if you recommend otherwise in your design)
Nice to have
• Some kind of background transparency combined with the pantone colour that gives the card some dimension and depth. But no gradient fills please :-)
Should not have
• Basic gradient fills
• Clipart

```html
<!DOCTYPE html>
<html lang="en">
<head>
<meta charset="utf-8">
<title>Velmora Business Card</title>
<link rel="stylesheet" href="https://fonts.googleapis.com/css2?family=Ubuntu:wght@400;500;700&family=Arimo:wght@400&display=swap">
<style>
  :root {
    --brand-red: #ac1c2c;
    --ink: #2e2e2e;
    --card-white: #f6f6f6;
    --backdrop: #e7e3df;
    --paper-white: #ffffff;
  }
  * { margin: 0; padding: 0; box-sizing: border-box; }
  html, body {
    width: 1200px;
    height: 900px;
    overflow: hidden;
    background: var(--backdrop);
  }
  .canvas {
    position: relative;
    width: 1200px;
    height: 900px;
  }
  .card {
    position: absolute;
    left: 376px;
    width: 444px;
    height: 278px;
    border-radius: 14px;
    overflow: hidden;
    box-shadow: 0 2px 6px rgba(0,0,0,0.18);
  }
  .card--front {
    top: 162px;
    background: var(--card-white);
    font-family: "Ubuntu", sans-serif;
    color: var(--ink);
  }
  .card--back {
    top: 471px;
    background: var(--brand-red);
  }
  .holder-name {
    position: absolute;
    left: 26px;
    top: 46px;
    font-size: 21px;
    font-weight: 400;
    letter-spacing: 0.1px;
  }
  .holder-role {
    position: absolute;
    left: 26px;
    top: 72px;
    font-size: 13.5px;
    color: var(--brand-red);
    text-transform: uppercase;
    letter-spacing: 0.2px;
  }
  .brand-name {
    position: absolute;
    right: 30px;
    top: 58px;
    font-size: 38px;
    font-weight: 700;
    color: var(--brand-red);
  }
  .website {
    position: absolute;
    right: 30px;
    top: 160px;
    font-size: 13.5px;
    font-style: italic;
    color: var(--brand-red);
  }
  .contact {
    position: absolute;
    left: 26px;
    top: 160px;
    font-size: 13.5px;
    line-height: 22px;
  }
  .company {
    position: absolute;
    left: 26px;
    top: 216px;
    font-size: 13.5px;
    line-height: 20px;
  }
  .company-name {
    font-weight: 700;
    color: var(--brand-red);
  }
  .back-brand {
    position: absolute;
    left: 76px;
    top: 106px;
    font-family: "Ubuntu", sans-serif;
    font-size: 54px;
    font-weight: 700;
    color: var(--paper-white);
    letter-spacing: -0.5px;
  }
  .tagline {
    position: absolute;
    left: 207px;
    top: 162px;
    font-family: "Arimo", sans-serif;
    font-size: 16px;
    color: var(--paper-white);
  }
</style>
</head>
<body>
<main class="canvas">
  <section class="card card--front" aria-label="Card front">
    <h1 class="holder-name">Daniel Marsh</h1>
    <p class="holder-role">Founder &amp; MD</p>
    <p class="brand-name">Velmora</p>
    <p class="website">www.velmora.com</p>
    <p class="contact">0825550143<br>daniel@velmora.com</p>
    <p class="company">
      <span class="company-name">Velmora (Pty) Ltd</span><br>
      Suite 210, 14 Ashford Rd. Parkhurst, JHB, RSA
    </p>
  </section>

  <section class="card card--back" aria-label="Card back">
    <p class="back-brand">Velmora</p>
    <p class="tagline">Strategic Innovation</p>
  </section>
</main>
</body>
</html>
```